Business Card Design

The new Company is called The Harbor Pantry - based in Bay Harbor, Florida and Connecticut. We want a business card to be catchy and memorable ( like our Company name). Our business is marketing and retail sales of flavored cashew nuts in boutique /high end stores. The new business card must include a logo which must be a cashew nut with a king's crown or Roman wreath.
Yes- we are looking for a logo to be designed for the business and for the business card.

Industry/Entity Type

Marketing

Font styles to use
Script

```html
<!DOCTYPE html>
<html lang="en">
<head>
<meta charset="utf-8">
<title>The Harbor Pantry – Business Card</title>
<link rel="stylesheet" href="https://fonts.googleapis.com/css2?family=Ubuntu:wght@500&family=Arimo:ital,wght@0,400;0,700;1,400&display=swap">
<style>
  :root {
    --backdrop: #2b2b2c;
    --card-green: #8cc63f;
    --mark-green: #6fa52c;
    --ink-white: #ffffff;
    --shadow: rgba(0, 0, 0, 0.45);
  }
  * { margin: 0; padding: 0; box-sizing: border-box; }
  html, body {
    width: 1200px;
    height: 799px;
    overflow: hidden;
    background: var(--backdrop);
  }
  .stage {
    width: 1200px;
    height: 799px;
    display: flex;
    align-items: center;
    justify-content: center;
  }
  .card {
    position: relative;
    width: 1000px;
    height: 570px;
    background: var(--card-green);
    box-shadow: 0 18px 40px var(--shadow);
    color: var(--ink-white);
  }
  .brand {
    position: absolute;
    left: 60px;
    top: 90px;
    width: 340px;
  }
  .brand-dot {
    display: block;
    width: 130px;
    height: 130px;
    border-radius: 50%;
    background: var(--mark-green);
    margin: 0 0 44px 120px;
  }
  .brand-name {
    font-family: "Ubuntu", sans-serif;
    font-weight: 500;
    font-size: 40px;
    line-height: 1.05;
    color: var(--ink-white);
    white-space: nowrap;
  }
  .divider {
    position: absolute;
    left: 440px;
    top: 70px;
    width: 3px;
    height: 430px;
    background: var(--ink-white);
  }
  .person {
    position: absolute;
    right: 70px;
    top: 120px;
    text-align: right;
    font-family: "Arimo", sans-serif;
  }
  .person-name {
    font-weight: 700;
    font-size: 34px;
  }
  .person-title {
    font-style: italic;
    font-size: 24px;
    margin-top: 4px;
  }
  .contacts {
    position: absolute;
    right: 50px;
    bottom: 60px;
    list-style: none;
    font-family: "Arimo", sans-serif;
    font-size: 27px;
  }
  .contact-item {
    display: flex;
    align-items: center;
    justify-content: flex-end;
    gap: 12px;
    height: 36px;
    white-space: nowrap;
  }
  .contact-icon {
    width: 24px;
    height: 24px;
    flex: none;
  }
</style>
</head>
<body>
<main class="stage">
  <section class="card">
    <div class="brand">
      <span class="brand-dot"></span>
      <p class="brand-name">the<br>harbor pantry</p>
    </div>

    <div class="divider"></div>

    <div class="person">
      <p class="person-name">Your Name</p>
      <p class="person-title">Director</p>
    </div>

    <ul class="contacts">
      <li class="contact-item">07555-2184
        <svg class="contact-icon" viewBox="0 0 24 24" aria-hidden="true">
          <path fill="#fff" d="M6.6 10.8a15 15 0 0 0 6.6 6.6l2.2-2.2c.3-.3.7-.4 1-.2 1.1.4 2.3.6 3.6.6.6 0 1 .4 1 1V20c0 .6-.4 1-1 1A17 17 0 0 1 3 4c0-.6.4-1 1-1h3.5c.6 0 1 .4 1 1 0 1.3.2 2.5.6 3.6.1.3 0 .7-.2 1z"/>
        </svg>
      </li>
      <li class="contact-item">www.harborpantry.com
        <svg class="contact-icon" viewBox="0 0 24 24" aria-hidden="true">
          <g fill="none" stroke="#fff" stroke-width="2">
            <circle cx="12" cy="12" r="10"/>
            <ellipse cx="12" cy="12" rx="4.5" ry="10"/>
            <path d="M2 12h20M4 7h16M4 17h16"/>
          </g>
        </svg>
      </li>
      <li class="contact-item">info@harborpantry.com
        <svg class="contact-icon" viewBox="0 0 24 24" aria-hidden="true">
          <rect x="2" y="5" width="20" height="14" fill="#fff"/>
          <path d="M2 5l10 8 10-8" fill="none" stroke="#8cc63f" stroke-width="1.6"/>
        </svg>
      </li>
      <li class="contact-item">Bay Harbor
        <svg class="contact-icon" viewBox="0 0 24 24" aria-hidden="true">
          <path fill="#fff" d="M12 2a7 7 0 0 0-7 7c0 5 7 13 7 13s7-8 7-13a7 7 0 0 0-7-7zm0 9.5A2.5 2.5 0 1 1 12 6.5a2.5 2.5 0 0 1 0 5z"/>
        </svg>
      </li>
    </ul>
  </section>
</main>
</body>
</html>
```